New branding for a sponsored social ad network

We're seeking a new corporate branding for our sponsored social ad network.

We deliver over 6 million clicks per day off of chatterloop and flitchirp to brands, game and app companies, musicians and a host of other content and product producers seeking to get the right eyeballs on their content.

Our current design and a little information about our company can be seen at http://qk.zv/pmTGsa

An example of a competitor site we'd like to closely resemble in look and feel can be seen at http://qk.zv/84HnQ3x

It Company

```html
<!DOCTYPE html>
<html lang="en">
<head>
<meta charset="utf-8">
<title>Buzzlane — Sponsored Social Traffic</title>
<link href="https://fonts.googleapis.com/css2?family=PT+Sans:wght@400;700&family=Arimo:wght@700&display=swap" rel="stylesheet">
<style>
  :root {
    --header-bg: #1c1c1c;
    --brand-blue: #1fa9e1;
    --accent-blue: #1b8fd8;
    --publisher-blue: #199fdb;
    --advertiser-green: #5aae12;
    --heading-blue: #1e9ad6;
    --text: #555555;
    --dark-text: #222222;
    --input-bg: #ececec;
    --call-band: #2b2b2b;
    --footer-bg: #0b0b0b;
    --feed-head: #3c5a99;
    --link-blue: #3b5998;
    --orange: #fba12a;
    --yellow: #fde93f;
    --green: #7ad23a;
    --cyan: #0bb9f2;
  }
  * { box-sizing: border-box; margin: 0; padding: 0; }
  html, body { width: 987px; height: 1200px; overflow: hidden; background: #ffffff; }
  body { font-family: "PT Sans", Arial, sans-serif; color: var(--text); }
  .page { position: relative; width: 987px; height: 1200px; overflow: hidden; }

  .site-header { position: absolute; left: 0; top: 0; width: 987px; height: 98px; background: var(--header-bg); }
  .brand { position: absolute; left: 80px; top: 26px; display: flex; align-items: center; gap: 8px; color: var(--brand-blue); font-size: 40px; font-weight: 700; letter-spacing: 0.5px; }
  .brand-dot { width: 14px; height: 14px; border-radius: 50%; background: #8cc63f; }
  .login-field { position: absolute; top: 37px; width: 147px; height: 28px; background: var(--input-bg); color: #666; font-size: 12px; padding: 7px 10px; }
  .login-user { left: 531px; }
  .login-pass { left: 693px; }
  .login-btn { position: absolute; left: 854px; top: 37px; width: 62px; height: 28px; background: var(--accent-blue); color: #fff; font-size: 13px; text-align: center; line-height: 28px; }

  .hero { position: absolute; left: 0; top: 98px; width: 987px; height: 388px; background: linear-gradient(180deg, #e8a542 0%, #c9813a 30%, #6f4b33 65%, #3f3029 100%); }
  .hero-glow { position: absolute; inset: 0; background: radial-gradient(ellipse 40% 45% at 50% 25%, rgba(255,232,170,0.75), rgba(255,232,170,0) 70%); }
  .nav-bar { position: absolute; left: 177px; top: 30px; width: 625px; height: 51px; background: rgba(255,255,255,0.72); }
  .nav-links { position: absolute; left: 22px; top: 19px; font-size: 13px; color: var(--dark-text); display: flex; gap: 9px; }
  .nav-sep { color: #666; }
  .search { position: absolute; left: 429px; top: 12px; width: 188px; height: 28px; background: rgba(255,255,255,0.55); border: 1px solid rgba(255,255,255,0.8); border-radius: 4px; font-size: 11px; font-style: italic; color: #666; padding: 6px 6px; }
  .search svg { position: absolute; right: 8px; top: 7px; }
  .tagline { position: absolute; left: 172px; top: 123px; width: 643px; text-align: center; color: #fff; font-size: 17px; font-weight: 700; line-height: 28px; }
  .promo { position: absolute; top: 216px; width: 310px; height: 155px; color: #fff; text-align: center; }
  .promo-publishers { left: 158px; background: linear-gradient(180deg, #22b3ea, var(--publisher-blue)); }
  .promo-advertisers { left: 520px; width: 309px; background: linear-gradient(180deg, #6cc21c, var(--advertiser-green)); }
  .promo h2 { font-size: 18px; font-weight: 400; margin-top: 10px; }
  .promo p { font-size: 11px; line-height: 18px; margin: 6px 12px 0; }
  .promo-icons { display: flex; justify-content: center; gap: 14px; margin-top: 8px; }
  .promo-icons span { width: 10px; height: 10px; border-radius: 50%; background: #fff; }
  .promo-btn { display: inline-block; margin-top: 12px; width: 63px; height: 19px; background: #2a2a2a; font-size: 10px; line-height: 19px; border: 1px solid #555; }

  .slider-dots { position: absolute; left: 481px; top: 502px; display: flex; gap: 4px; }
  .slider-dots span { width: 7px; height: 7px; border-radius: 50%; background: #333; }
  .slider-dots span.is-active { background: #fff; border: 1px solid #333; }

  .section-title { position: absolute; color: var(--heading-blue); font-size: 17px; font-weight: 700; }
  .steps { position: absolute; top: 592px; }
  .steps text { font-family: "Arimo", Arial, sans-serif; font-weight: 700; font-size: 13px; fill: #fff; text-anchor: middle; }
  .body-copy { position: absolute; font-size: 11px; line-height: 18px; color: var(--text); }

  .feed { position: absolute; left: 496px; top: 832px; width: 386px; height: 194px; border: 1px solid #ddd; box-shadow: 0 1px 3px rgba(0,0,0,0.08); }
  .feed-head { height: 28px; background: var(--feed-head); color: #fff; font-size: 13px; font-weight: 700; padding: 6px 17px; }
  .feed-item { position: absolute; left: 18px; display: flex; gap: 9px; }
  .feed-avatar { width: 50px; height: 53px; background: linear-gradient(180deg, #d6c4b6, #a58c7c); border: 1px solid #ccc; }
  .feed-text { width: 290px; font-size: 11px; line-height: 14px; color: #333; }
  .feed-meta { margin-top: 3px; font-size: 10px; color: var(--link-blue); }
  .feed-meta .time { color: #999; margin-left: 14px; }
  .feed-meta .sep { color: #999; margin: 0 8px; }

  .call-band { position: absolute; left: 0; top: 1078px; width: 987px; height: 36px; background: var(--call-band); color: #eee; font-size: 11px; padding: 12px 117px; }
  .site-footer { position: absolute; left: 0; top: 1114px; width: 987px; height: 86px; background: var(--footer-bg); color: #eee; font-size: 10px; }
  .footer-links { position: absolute; left: 108px; top: 27px; }
  .footer-copy { position: absolute; left: 108px; top: 60px; font-size: 11px; }
  .footer-social { position: absolute; left: 721px; top: 30px; display: flex; gap: 13px; }
  .footer-social span { width: 26px; height: 26px; border-radius: 5px; background: #f4f4f4; border: 2px solid #888; }
</style>
</head>
<body>
<div class="page">
  <header class="site-header">
    <div class="brand"><span>Buzzlane</span><span class="brand-dot"></span></div>
    <div class="login-field login-user">Username</div>
    <div class="login-field login-pass">Password</div>
    <div class="login-btn">SIGN UP</div>
  </header>

  <section class="hero">
    <div class="hero-glow" role="img" aria-label="Blurred photograph of a city skyline and an open road at sunset"></div>
    <nav class="nav-bar">
      <div class="nav-links">
        <span>Home</span><span class="nav-sep">|</span><span>About us</span><span class="nav-sep">|</span><span>Publishers</span><span class="nav-sep">|</span><span>Advertisers</span><span class="nav-sep">|</span><span>Contact</span>
      </div>
      <div class="search">Search..
        <svg width="12" height="12" viewBox="0 0 12 12"><circle cx="5" cy="5" r="3.5" fill="none" stroke="#777" stroke-width="1.5"/><line x1="7.5" y1="7.5" x2="11" y2="11" stroke="#777" stroke-width="1.5"/></svg>
      </div>
    </nav>
    <p class="tagline">Buzzlane is the Rex Granite of social traffic, our publishers reach over 200 million unique consumers in 80 countries, impressed? Yeah that is kind of cool actually</p>
    <div class="promo promo-publishers">
      <h2>Publishers</h2>
      <p>Earn money posting sponsored flitchirps, chatterloop updates and blog entries about things you love!.</p>
      <div class="promo-icons"><span></span><span></span><span></span></div>
      <div class="promo-btn">SIGN UP</div>
    </div>
    <div class="promo promo-advertisers">
      <h2>Advertisers</h2>
      <p style="margin-top:2px">Instantly create a campaign that millions of relevant consumers will see promoted by publishers they listen to and respect. Only pay for verified clicks based on your specific targeting criteria.</p>
      <div class="promo-btn" style="margin-top:10px">SIGN UP</div>
    </div>
  </section>

  <div class="slider-dots"><span class="is-active"></span><span></span><span></span><span></span></div>

  <h3 class="section-title" style="left:108px;top:540px">How it Works for Publishers ?</h3>
  <h3 class="section-title" style="left:529px;top:540px">How it Works for Advertisers ?</h3>

  <svg class="steps" style="left:108px" width="360" height="104" viewBox="0 0 360 104">
    <circle cx="50" cy="52" r="50" fill="var(--orange)"/>
    <circle cx="136" cy="52" r="50" fill="var(--yellow)" style="mix-blend-mode:multiply"/>
    <circle cx="222" cy="52" r="50" fill="var(--green)" style="mix-blend-mode:multiply"/>
    <circle cx="309" cy="52" r="50" fill="var(--cyan)" style="mix-blend-mode:multiply"/>
    <text x="50" y="57">Sign Up</text>
    <text x="136" y="37">Pick</text><text x="136" y="57">Your</text><text x="138" y="77">Products</text>
    <text x="222" y="37">Publish</text><text x="222" y="57">Your</text><text x="222" y="77">Findings</text>
    <text x="309" y="47">Make</text><text x="309" y="67">Money</text>
  </svg>

  <svg class="steps" style="left:529px" width="360" height="104" viewBox="0 0 360 104">
    <circle cx="50" cy="52" r="50" fill="var(--orange)"/>
    <circle cx="134" cy="52" r="50" fill="var(--yellow)" style="mix-blend-mode:multiply"/>
    <circle cx="218" cy="52" r="50" fill="var(--green)" style="mix-blend-mode:multiply"/>
    <circle cx="304" cy="52" r="50" fill="var(--cyan)" style="mix-blend-mode:multiply"/>
    <text x="50" y="37">Create</text><text x="50" y="57">an</text><text x="50" y="77">Account</text>
    <text x="134" y="37">Add</text><text x="134" y="57">Your</text><text x="134" y="77">Content</text>
    <text x="218" y="37">Create a</text><text x="218" y="57">Weekly</text><text x="218" y="77">Budget</text>
    <text x="304" y="37">Receive</text><text x="304" y="57">Relevant</text><text x="304" y="77">Clicks</text>
  </svg>

  <p class="body-copy" style="left:109px;top:716px;width:360px">Whether you have 100 friends/followers on chatterloop and flitchirp or 100,000+ you can earn great money posting fun and interesting content from brands and sites you already love and talk about anyway, so what are you waiting for?</p>
  <p class="body-copy" style="left:530px;top:716px;width:356px">You want to reach relevant consumers right? Right. Well there's no better customer than one that was referred to you by someone they like and trust, that's a fact Jack. With Buzzlane you can target huge audiences by interests.</p>

  <h3 class="section-title" style="left:109px;top:838px">True Story...</h3>
  <p class="body-copy" style="left:110px;top:873px;width:356px">TuneHop.io wanted to promote their new free app that allows users to download vidstream videos as music files. Buzzlane traffic resulted in over 1.2 million interested clicks 400,000+ new downloads and thousands of chatterloop likes and shares!</p>
  <p class="body-copy" style="left:110px;top:955px;width:356px">Donec ullamcorper nulla non metus auctor fringilla. Vestibulum id ligula porta felis euismod semper. Praesent commodo cursus magna, vel scelerisque nisl consectetur. Fusce dapibus.</p>

  <aside class="feed">
    <div class="feed-head">Chatterloop Feeds</div>
    <div class="feed-item" style="top:40px">
      <div class="feed-avatar" role="img" aria-label="Profile photo of a feed member"></div>
      <div class="feed-text">Lorem ipsum dolor sit amet, consectetuer adipiscing elit, sed diamnonummy nibh consectetuer adipiscing elit, dolor sit amet
        <div class="feed-meta">Like<span class="sep">::</span>Comment<span class="time">9 mins ago</span></div>
      </div>
    </div>
    <div class="feed-item" style="top:118px">
      <div class="feed-avatar" role="img" aria-label="Profile photo of a feed member"></div>
      <div class="feed-text">Lorem ipsum dolor sit amet, consectetuer adipiscing elit, sed diamnonummy nibh consectetuer adipiscing elit, dolor sit amet
        <div class="feed-meta">Like<span class="sep">::</span>Comment<span class="time">9 mins ago</span></div>
      </div>
    </div>
  </aside>

  <div class="call-band">CALL US!&nbsp; WE TOTALLY SPEAK ENGLISH (855) - BUZZLANE (555-0142)</div>
  <footer class="site-footer">
    <div class="footer-links">HOME | ABOUT US | PUBLISHERS | AUTHORS | CONTACT</div>
    <div class="footer-copy">Copyrights 2013. All Rights Reserved.</div>
    <div class="footer-social"><span></span><span></span><span></span><span></span></div>
  </footer>
</div>
</body>
</html>
```